How likely are people to engage in social distancing? We need a good illustration to show the data!

We surveyed U.S. adults March 20th - 24th, 2020 and asked how likely they were to engage in social distancing (and other COVID-19 related health behaviors). What did the survey find? Basically, most people intend to engage in social distancing behaviors (e.g., avoiding large crowds) and other behaviors that reduce the spread of COVID-19 (e.g., washing hands at least 20 seconds). When most people intend to engage in a behavior, then public health professionals try to leverage that to move more people to act.
Now we need innovative and professional images that attempt to communicate one or all of these findings. The specific findings are nicely summarized in the attached document. For example, 82% of participants intend to engage in social distancing.
What sort of visual are we looking for? Our preference is for an original illustration (or set of illustrations). Our preference is for (creative and powerful illustrations, but we are also open to the creative and well-executed infographics.
We need these images fast . We will award monetary prizes to the 3 best designs. If we like more than that, then we might purchase more (e.g., in past contests, we have purchased as many as 30 designs).
What we will need:
(1) The illustrations must be original and we will need the photoshop and/or illustrator files for all artwork.
(2) You can illustrate all of the findings or just one of them. We need creative approaches that do a lucid job of bringing the data to life. Most people intend to engage in these behaviors. How to communicate that? Corvantists and Halmerites do not differ in their intentions; how to communicate that?
(3) The illustration should say, somewhere: "Based on a survey of 400 U.S. adults conducted March 20 - 24th, 2020."

U.S. Adults

• Original illustrations based on the findings of the survey (see attached document).

```html
<!DOCTYPE html>
<html lang="en">
<head>
<meta charset="utf-8">
<title>Corvantists vs Halmerites — Intentions to Slow the Spread</title>
<link rel="stylesheet" href="https://fonts.googleapis.com/css2?family=Chakra+Petch:wght@600;700&family=Exo+2:wght@300;500;600&display=swap">
<style>
  :root {
    --ink: #000000;
    --paper: #ffffff;
    --party-red: #be1e2d;
    --party-blue: #00aeef;
    --label-grey: #6d6e71;
    --title-ink: #111111;
  }
  * { margin: 0; padding: 0; box-sizing: border-box; }
  html, body { width: 927px; height: 1200px; overflow: hidden; background: var(--paper); }
  .poster { position: relative; width: 927px; height: 1200px; background: var(--paper); }

  .masthead { position: absolute; left: 0; top: 0; width: 927px; height: 398px; background: var(--ink); overflow: hidden; }
  .virus-art {
    position: absolute; left: 0; top: 0; width: 600px; height: 398px;
    background: radial-gradient(circle at 258px 210px, #3a3a3a 0, #1c1c1c 55%, #000000 100%);
  }
  .versus-disc {
    position: absolute; left: 89px; top: 41px; width: 338px; height: 338px;
    border-radius: 50%; background: var(--paper);
  }
  .versus-title {
    position: absolute; left: 89px; top: 141px; width: 338px; text-align: center;
    font-family: "Chakra Petch", sans-serif; font-weight: 700; line-height: 1;
  }
  .versus-title .party { display: block; font-size: 44px; letter-spacing: 0.5px; }
  .versus-title .party-red { color: var(--party-red); }
  .versus-title .party-blue { color: var(--party-blue); }
  .versus-title .vs { display: block; font-size: 40px; color: var(--ink); margin: 6px 0 4px; }

  .question {
    position: absolute; left: 548px; top: 70px; width: 366px; text-align: center;
    font-family: "Exo 2", sans-serif; font-weight: 500; color: var(--paper);
    font-size: 30px; line-height: 33px; letter-spacing: 0.4px;
  }
  .survey-note {
    position: absolute; left: 548px; top: 276px; width: 366px; text-align: center;
    font-family: "Chakra Petch", sans-serif; font-weight: 600; color: var(--paper);
    font-size: 12.5px; line-height: 15px;
  }

  .chart { position: absolute; left: 0; top: 398px; width: 927px; height: 673px; }
  .chart .behaviour { font-family: "Exo 2", sans-serif; font-weight: 600; font-size: 42px; fill: var(--title-ink); letter-spacing: 1.5px; }
  .chart .share { font-family: "Exo 2", sans-serif; font-weight: 300; font-size: 36px; fill: var(--label-grey); letter-spacing: 2px; }
  .chart .red { fill: var(--party-red); }
  .chart .blue { fill: var(--party-blue); }

  .verdict {
    position: absolute; left: 0; top: 1071px; width: 927px; height: 129px; background: var(--ink);
    font-family: "Chakra Petch", sans-serif; font-weight: 700; color: var(--paper);
    font-size: 92px; line-height: 129px; text-align: center; letter-spacing: -1px; white-space: nowrap;
  }
</style>
</head>
<body>
<main class="poster">
  <header class="masthead">
    <div class="virus-art" role="img" aria-label="Line illustration of a coronavirus particle with radiating spikes"></div>
    <div class="versus-disc"></div>
    <h1 class="versus-title">
      <span class="party party-red">Corvantists</span>
      <span class="vs">vs</span>
      <span class="party party-blue">Halmerites</span>
    </h1>
    <p class="question">How likely it is<br>that they will perform<br>these behaviors<br>to slow the spread<br>of coronavirus?</p>
    <p class="survey-note">Based on a survey of 400 U.S. adults<br>conducted March 20 – 24th, 2020.</p>
  </header>

  <svg class="chart" viewBox="0 725 1688 1225" xmlns="http://www.w3.org/2000/svg" aria-label="Share of each group likely to perform each behavior">
    <defs>
      <g id="full-row">
        <rect class="red" x="337" width="42" height="41"/><rect class="red" x="404" width="42" height="41"/>
        <rect class="red" x="470" width="42" height="41"/><rect class="red" x="537" width="42" height="41"/>
        <rect class="red" x="604" width="42" height="41"/><rect class="red" x="670" width="42" height="41"/>
        <rect class="red" x="737" width="42" height="41"/><rect class="red" x="803" width="42" height="41"/>
        <rect class="blue" x="845" width="42" height="41"/><rect class="blue" x="912" width="42" height="41"/>
        <rect class="blue" x="978" width="42" height="41"/><rect class="blue" x="1045" width="42" height="41"/>
        <rect class="blue" x="1111" width="42" height="41"/><rect class="blue" x="1178" width="42" height="41"/>
        <rect class="blue" x="1245" width="42" height="41"/><rect class="blue" x="1311" width="42" height="41"/>
      </g>
    </defs>

    <g class="row">
      <text class="behaviour" x="845" y="815" text-anchor="middle">Engage in social distancing</text>
      <text class="share" x="278" y="870" text-anchor="end">82%</text>
      <use href="#full-row" y="835"/>
      <rect class="red" x="305" y="835" width="7" height="41"/>
      <rect class="blue" x="1378" y="835" width="5" height="41"/>
      <text class="share" x="1413" y="870">81%</text>
    </g>

    <g class="row">
      <text class="behaviour" x="845" y="960" text-anchor="middle">Work from home</text>
      <text class="share" x="443" y="1015" text-anchor="end">60%</text>
      <rect class="red" x="470" y="980" width="42" height="41"/><rect class="red" x="537" y="980" width="42" height="41"/>
      <rect class="red" x="604" y="980" width="42" height="41"/><rect class="red" x="670" y="980" width="42" height="41"/>
      <rect class="red" x="737" y="980" width="42" height="41"/><rect class="red" x="803" y="980" width="42" height="41"/>
      <rect class="blue" x="845" y="980" width="42" height="41"/><rect class="blue" x="912" y="980" width="42" height="41"/>
      <rect class="blue" x="978" y="980" width="42" height="41"/><rect class="blue" x="1045" y="980" width="42" height="41"/>
      <rect class="blue" x="1111" y="980" width="42" height="41"/><rect class="blue" x="1178" y="980" width="42" height="41"/>
      <rect class="blue" x="1245" y="980" width="20" height="41"/>
      <text class="share" x="1293" y="1015">65%</text>
    </g>

    <g class="row">
      <text class="behaviour" x="845" y="1103" text-anchor="middle">Avoid large gatherings</text>
      <text class="share" x="262" y="1160" text-anchor="end">85%</text>
      <use href="#full-row" y="1125"/>
      <rect class="red" x="291" y="1125" width="21" height="41"/>
      <rect class="blue" x="1378" y="1125" width="17" height="41"/>
      <text class="share" x="1423" y="1160">84%</text>
    </g>

    <g class="row">
      <text class="behaviour" x="845" y="1245" text-anchor="middle">Cancel social activities</text>
      <text class="share" x="276" y="1305" text-anchor="end">82%</text>
      <use href="#full-row" y="1270"/>
      <rect class="red" x="305" y="1270" width="7" height="41"/>
      <text class="share" x="1382" y="1305">80%</text>
    </g>

    <g class="row">
      <text class="behaviour" x="845" y="1396" text-anchor="middle">Put distance between self and other people</text>
      <text class="share" x="268" y="1450" text-anchor="end">84%</text>
      <use href="#full-row" y="1415"/>
      <rect class="red" x="296" y="1415" width="16" height="41"/>
      <rect class="blue" x="1378" y="1415" width="30" height="41"/>
      <text class="share" x="1441" y="1452">87%</text>
    </g>

    <g class="row">
      <text class="behaviour" x="845" y="1542" text-anchor="middle">Wash hands at least 20 seconds</text>
      <text class="share" x="253" y="1592" text-anchor="end">87%</text>
      <use href="#full-row" y="1560"/>
      <rect class="red" x="283" y="1560" width="29" height="41"/>
      <rect class="blue" x="1378" y="1560" width="33" height="41"/>
      <text class="share" x="1440" y="1594">88%</text>
    </g>

    <g class="row">
      <text class="behaviour" x="845" y="1683" text-anchor="middle">Use hand sanitizer</text>
      <text class="share" x="253" y="1738" text-anchor="end">87%</text>
      <use href="#full-row" y="1705"/>
      <rect class="red" x="283" y="1705" width="29" height="41"/>
      <rect class="blue" x="1378" y="1705" width="17" height="41"/>
      <text class="share" x="1423" y="1740">84%</text>
    </g>

    <g class="row">
      <text class="behaviour" x="845" y="1830" text-anchor="middle">Avoid touching your eyes, nose, and mouth</text>
      <text class="share" x="308" y="1885" text-anchor="end">80%</text>
      <use href="#full-row" y="1850"/>
      <rect class="blue" x="1378" y="1850" width="8" height="41"/>
      <text class="share" x="1417" y="1887">82%</text>
    </g>
  </svg>

  <footer class="verdict">NO big difference!</footer>
</main>
</body>
</html>
```